Book cover for LM

Design cover for a book of gratitude and inspiration.
Book trim size will be 6.5 x 6.5 inches, or 8 x 8 inches, hardcover, 96 pages
Title: Lantern Meadows
Subtitle: A Book of Gratitude and Inspiration
Author: Gus Halverd

```html
<!DOCTYPE html>
<html lang="en">
<head>
<meta charset="utf-8">
<title>Lantern Meadows – Book Cover</title>
<link rel="stylesheet" href="https://fonts.googleapis.com/css2?family=Playfair+Display:wght@500;600&family=Mr+Dafoe&family=Yellowtail&display=swap">
<style>
  :root {
    --page-bg: #ffffff;
    --title-brown: #5a3420;
    --script-brown: #4e2d1c;
    --text-light: #fffaf0;
    --glow-white: #fff6d8;
    --glow-gold: #ffcf5a;
    --warm-cream: #efdcb4;
    --wall-beige: #d8bd8c;
    --amber: #e99a2c;
    --bronze: #a0642c;
    --deep-rust: #8e3b18;
  }
  * { margin: 0; padding: 0; box-sizing: border-box; }
  html, body {
    width: 830px;
    height: 1200px;
    overflow: hidden;
    background: var(--page-bg);
  }
  .canvas {
    position: relative;
    width: 830px;
    height: 1200px;
  }
  .cover {
    position: absolute;
    left: 55px;
    top: 240px;
    width: 720px;
    height: 720px;
    overflow: hidden;
    box-shadow: 0 6px 18px rgba(0,0,0,0.12);
  }
  .cover-photo {
    position: absolute;
    inset: 0;
    background:
      /* glowing garland band sweeping from the left middle to the lower right */
      radial-gradient(ellipse 70px 55px at 150px 300px, rgba(255,246,216,0.85), rgba(255,207,90,0) 100%),
      radial-gradient(ellipse 110px 70px at 230px 360px, rgba(255,236,170,0.9), rgba(255,207,90,0) 100%),
      radial-gradient(ellipse 140px 90px at 370px 420px, rgba(255,226,140,0.85), rgba(255,190,70,0) 100%),
      radial-gradient(ellipse 150px 110px at 520px 470px, rgba(255,214,100,0.95), rgba(255,180,50,0) 100%),
      radial-gradient(ellipse 130px 170px at 660px 380px, rgba(255,220,110,0.9), rgba(255,180,50,0) 100%),
      radial-gradient(ellipse 170px 110px at 610px 610px, rgba(255,200,70,0.9), rgba(240,150,30,0) 100%),
      radial-gradient(ellipse 120px 60px at 330px 510px, rgba(180,100,40,0.35), rgba(180,100,40,0) 100%),
      radial-gradient(ellipse 90px 50px at 560px 300px, rgba(160,90,40,0.3), rgba(160,90,40,0) 100%),
      radial-gradient(circle at 40% 45%, rgba(255,238,190,0.6), rgba(255,238,190,0) 35%),
      radial-gradient(circle at 8% 98%, rgba(142,59,24,0.75), rgba(142,59,24,0) 30%),
      radial-gradient(circle at 100% 100%, rgba(170,60,20,0.85), rgba(170,60,20,0) 30%),
      linear-gradient(180deg, var(--wall-beige) 0%, var(--warm-cream) 22%, #f0d7a0 55%, #e3b36a 78%, var(--bronze) 92%, var(--deep-rust) 100%);
  }
  .title { font-weight: normal; }
  .title-serif {
    position: absolute;
    top: 55px;
    left: 0;
    width: 100%;
    text-align: center;
    font-family: "Playfair Display", serif;
    font-weight: 600;
    font-size: 118px;
    line-height: 1;
    letter-spacing: -1px;
    color: var(--title-brown);
    transform: scaleX(0.74);
  }
  .title-script {
    position: absolute;
    top: 160px;
    left: 30px;
    width: 100%;
    text-align: center;
    font-family: "Mr Dafoe", cursive;
    font-size: 140px;
    line-height: 1;
    color: var(--script-brown);
  }
  .subtitle {
    position: absolute;
    left: 82px;
    top: 562px;
    font-family: "Playfair Display", serif;
    font-weight: 500;
    font-size: 33px;
    line-height: 36px;
    color: var(--text-light);
  }
  .author {
    position: absolute;
    left: 508px;
    top: 616px;
    color: var(--text-light);
  }
  .author-label {
    font-family: "Playfair Display", serif;
    font-weight: 500;
    font-size: 18px;
    line-height: 1;
  }
  .author-name {
    font-family: "Yellowtail", cursive;
    font-size: 34px;
    line-height: 1.15;
    margin-left: -2px;
  }
</style>
</head>
<body>
  <main class="canvas">
    <section class="cover">
      <div class="cover-photo" role="img" aria-label="Warm golden photograph of a vine of leaves woven with glowing fairy lights sweeping across a textured cream wall"></div>
      <h1 class="title">
        <span class="title-serif">LANTERN</span>
        <span class="title-script">Meadows</span>
      </h1>
      <p class="subtitle">A Book<br>of Gratitude &amp;<br>Inspiration</p>
      <div class="author">
        <p class="author-label">Author</p>
        <p class="author-name">Gus Halverd</p>
      </div>
    </section>
  </main>
</body>
</html>
```